External newsletter design for a consulting firm

We are a workforce development and consulting organisation. Requirements - contemporary design for a newsletter to address to our external audiences.
Easy to read and load.
I have uploaded the content and a dummy newsletter (We are looking for a fresher and more modern feel)

Target Market(s)

IT professionals, Company Quality and Training heads

Industry/Entity Type

Consulting

Colors

Designer to choose colors to be used in the design.

```html
<!DOCTYPE html>
<html lang="en">
<head>
<meta charset="utf-8">
<title>Qualtis Newsletter</title>
<link href="https://fonts.googleapis.com/css2?family=Titillium+Web:wght@300;400;600;700&display=swap" rel="stylesheet">
<style>
  :root {
    --page-bg: #ecebeb;
    --white: #ffffff;
    --brand-purple: #2e1f8a;
    --brand-orange: #ff9000;
    --ink: #1f1f1f;
    --ink-soft: #333333;
  }
  * { box-sizing: border-box; margin: 0; padding: 0; }
  html, body {
    width: 1200px; height: 900px; overflow: hidden;
    background: var(--page-bg);
    font-family: "Titillium Web", Arial, sans-serif;
  }
  .newsletter {
    position: absolute; left: 285px; top: 0; width: 600px;
  }
  .article-panel {
    background: var(--white); height: 362px; position: relative;
  }
  .cta-button {
    position: absolute; left: 213px; top: 25px; width: 165px; height: 48px;
    background: var(--brand-orange); color: var(--white);
    font-weight: 700; font-size: 15px; letter-spacing: 0.2px;
    display: flex; align-items: center; justify-content: center;
    text-decoration: none;
  }
  .story { position: absolute; left: 29px; top: 106px; width: 540px; }
  .story-number {
    position: absolute; left: 0; top: 0; width: 31px; height: 31px; border-radius: 50%;
    background: var(--brand-orange); color: var(--white);
    font-weight: 700; font-size: 18px; line-height: 31px; text-align: center;
  }
  .story-title {
    position: absolute; left: 46px; top: -1px; line-height: 31px;
    font-size: 20px; font-weight: 700; color: var(--brand-purple); white-space: nowrap;
  }
  .story-body {
    position: absolute; left: 48px; top: 44px; width: 475px;
    font-size: 16px; font-weight: 300; line-height: 24px; color: var(--ink);
  }
  .wins-panel {
    background: var(--brand-purple); height: 290px; padding: 34px 0 0 75px; color: var(--white);
  }
  .wins-title { font-size: 20px; font-weight: 700; line-height: 28px; margin-bottom: 15px; }
  .wins-list { list-style: none; padding-left: 1px; width: 470px; }
  .wins-list li { font-size: 16px; line-height: 24px; margin-bottom: 12px; }
  .footer-bar {
    height: 96px; display: flex; align-items: center; justify-content: space-between;
  }
  .social-links { display: flex; gap: 22px; padding-left: 12px; }
  .social-links a {
    color: var(--brand-purple); font-weight: 700; font-size: 14px; text-decoration: none;
  }
  .brand-name {
    font-size: 38px; font-weight: 400; color: var(--ink); letter-spacing: 0.5px; line-height: 1;
  }
  .legal-text {
    font-size: 11.7px; line-height: 14.5px; color: var(--ink-soft); margin-top: 5px; width: 598px;
  }
  .unsubscribe {
    display: block; width: max-content; margin: 22px auto 0;
    font-size: 12px; font-weight: 700; color: var(--brand-purple);
    text-decoration: underline;
  }
</style>
</head>
<body>
  <main class="newsletter">
    <section class="article-panel">
      <a class="cta-button" href="#">READ MORE HERE</a>
      <article class="story">
        <span class="story-number">3</span>
        <h2 class="story-title">8th annual VERITY conference in Washington DC</h2>
        <p class="story-body">Qualtis Global Institute presented the Verified Engineering and Reliable IT Testing Conference (VERITY), a premier IT conference, expo and classroom training experience in Baltimore, Washington DC. This annual event provides opportunities to Learn, Assess, Apply and Connect managers and practitioners in project management, software development, QA testing and process engineering.</p>
      </article>
    </section>

    <section class="wins-panel">
      <h2 class="wins-title">Recent Wins</h2>
      <ul class="wins-list">
        <li>Nordvale Software - Mastering Agile Scrum Training</li>
        <li>Brightpath Datasystems - PMMI Dev V 1.3 ML 3</li>
        <li>Northland Revenue Office - CTSP certification</li>
        <li>Halvorsen Electric India - Competency Development Program (Corvin Testing Institute)</li>
      </ul>
    </section>

    <footer>
      <div class="footer-bar">
        <nav class="social-links">
          <a href="#">Follow</a>
          <a href="#">Share</a>
          <a href="#">Connect</a>
        </nav>
        <span class="brand-name">Qualtis</span>
      </div>
      <p class="legal-text">SEQM, PMMI© Lorem ipsum dolor sit amet, consectetuer adipiscing elit. Phasellus hendrerit. Pellentesque aliquet nibh nec urna. In nisi neque, aliquet vel, dapibus id, mattis vel, nisi. Sed pretium, ligula sollicitudin laoreet viverra, tortor libero sodales leo, eget blandit nunc tortor eu nibh. Nullam mollis. Ut justo. Suspendisse potenti.</p>
      <a class="unsubscribe" href="#">Unsubscribe</a>
    </footer>
  </main>
</body>
</html>
```